Marlowin Extra Virgin Olive Oil

We need a label design for a funky Australian Extra Virgin olive oil which will target exclusively female customers that wish to utilise the product for health and beauty. We need it to have a fun and sexy modern design and it must feature an image either photo/animation/abstract or caricature of a healthy young woman. The image must be able to be used royalty free. The Olive Oil is called MARLOWIN.

The label is for a 250ml bottle. The label size is 154mm high x 50mm Wide

I have attached the type of bottle and a couple of images just to point in the right direction.

```html
<!DOCTYPE html>
<html lang="en">
<head>
<meta charset="utf-8">
<title>Marlowin Extra Virgin Olive Oil – Bottle Label</title>
<link rel="stylesheet" href="https://fonts.googleapis.com/css2?family=Jost:wght@400;500;600&display=swap">
<style>
  :root {
    --page-bg: #ffffff;
    --label-mat: #f3f3f3;
    --label-paper: #ffffff;
    --label-border: #9a9a9a;
    --ink: #1c1c1c;
    --olive-green: #9fba62;
    --leaf-tone: #6f9a3a;
    --photo-backdrop: #f2ede7;
    --photo-skin: #d8b397;
    --photo-top: #ece4da;
    --photo-table: #eef0e6;
    --photo-salad: #b9cf8f;
  }
  * { box-sizing: border-box; margin: 0; padding: 0; }
  html, body {
    width: 1200px;
    height: 944px;
    overflow: hidden;
    background: var(--page-bg);
  }
  body {
    position: relative;
    font-family: "Jost", "Futura", sans-serif;
    color: var(--ink);
  }
  .label-mat {
    position: absolute;
    left: 460px;
    top: 52px;
    width: 280px;
    height: 840px;
    background: var(--label-mat);
  }
  .label {
    position: absolute;
    left: 8px;
    top: 8px;
    width: 264px;
    height: 824px;
    background: var(--label-paper);
    border: 1.5px solid var(--label-border);
    border-radius: 3px;
  }
  .label__emblem {
    position: absolute;
    left: 97px;
    top: 52px;
    width: 70px;
    height: 70px;
    border-radius: 50%;
    background: radial-gradient(circle, var(--leaf-tone) 0%, #a9c47e 55%, rgba(255,255,255,0) 72%);
  }
  .label__brand {
    position: absolute;
    left: 0;
    right: 0;
    top: 188px;
    text-align: center;
    font-size: 36px;
    font-weight: 400;
    letter-spacing: 4px;
    line-height: 1;
  }
  .label__variety {
    position: absolute;
    left: 22px;
    right: 22px;
    top: 240px;
    display: flex;
    align-items: center;
    gap: 10px;
    font-size: 19px;
    font-weight: 400;
    line-height: 1;
  }
  .label__variety::before,
  .label__variety::after {
    content: "";
    flex: 1;
    height: 2px;
    background: var(--olive-green);
  }
  .label__product {
    position: absolute;
    left: 0;
    right: 0;
    top: 273px;
    text-align: center;
    font-size: 23px;
    font-weight: 400;
    letter-spacing: 3px;
    line-height: 1;
  }
  .label__photo {
    position: absolute;
    left: 18px;
    right: 18px;
    top: 360px;
    height: 268px;
    background: linear-gradient(180deg,
      var(--photo-backdrop) 0%,
      var(--photo-skin) 30%,
      var(--photo-top) 55%,
      var(--photo-skin) 72%,
      var(--photo-salad) 84%,
      var(--photo-table) 94%,
      var(--label-paper) 100%);
  }
  .label__origin {
    position: absolute;
    left: 0;
    right: 0;
    top: 700px;
    text-align: center;
    font-size: 18px;
    font-weight: 600;
    line-height: 1.25;
    color: var(--olive-green);
  }
  .label__volume {
    position: absolute;
    right: 14px;
    top: 770px;
    font-size: 25px;
    font-weight: 500;
    line-height: 1;
  }
</style>
</head>
<body>
  <div class="label-mat">
    <section class="label">
      <div class="label__emblem" role="img" aria-label="Olive branch with leaves and black olives"></div>
      <h1 class="label__brand">MARLOWIN</h1>
      <p class="label__variety">Extra Virgin</p>
      <p class="label__product">- OLIVE OIL -</p>
      <div class="label__photo" role="img" aria-label="Photo of a smiling young woman in a white top seated at a table with a plate of fresh salad"></div>
      <p class="label__origin">100% NATURAL<br>AUSTRALIAN PRODUCT</p>
      <p class="label__volume">250ml.</p>
    </section>
  </div>
</body>
</html>
```